Tri fold flyer design for restoration company

Use our website for inspiration and make a world class advertising tri fold flyer.
brookvalerestoration.com

Colors
0054AA
0677BA
7BADD7
CADEEF
E8F1F8
00AB8E
00BBA5
67D7C9
C6EFE9
E9F9F6
EB3D1F
EC4F4E
F09395
F8D3D4
FCEDEE

```html
<!DOCTYPE html>
<html lang="en">
<head>
<meta charset="utf-8">
<title>Brookvale Restoration – Tri-fold Flyer</title>
<link href="https://fonts.googleapis.com/css2?family=Montserrat:wght@400;500;600;700;800;900&display=swap" rel="stylesheet">
<style>
:root{
  --blue:#0a4aa0;
  --blue-deep:#003f8f;
  --orange:#e5461a;
  --orange-deep:#b63d0d;
  --paper:#f1f1f1;
  --paper-shade:#d9d9d9;
  --ink:#2b2b2b;
  --white:#ffffff;
  --stage:#e9ecef;
}
*{box-sizing:border-box;margin:0;padding:0}
html,body{width:1200px;height:800px;overflow:hidden}
body{background:var(--stage);font-family:"Montserrat",sans-serif;color:var(--ink);position:relative}
.spread{position:absolute;top:190px;width:570px;height:420px;display:flex;box-shadow:0 6px 18px rgba(0,0,0,.18)}
.spread--outside{left:20px}
.spread--inside{left:610px}
.panel{position:relative;width:190px;height:420px;overflow:hidden;background:linear-gradient(135deg,var(--paper),var(--paper-shade))}
.panel + .panel{box-shadow:inset 1px 0 0 rgba(0,0,0,.08)}
.panel__shapes{position:absolute;inset:0;width:190px;height:420px}
.abs{position:absolute}
.photo{position:absolute;overflow:hidden}
.photo--framed{border:2px solid var(--orange)}
.h-panel{font-weight:800;font-size:10px;line-height:1.15}
.rule{display:block;width:22px;height:2px;background:var(--orange);margin:4px 0 5px}
.copy{font-size:5.6px;line-height:1.45;font-weight:500}
.copy p + p{margin-top:3px}

/* Crime scene panel */
.crime{left:14px;top:22px;width:162px;color:var(--white)}
.steps{position:absolute;left:14px;top:114px;width:162px;color:var(--white);list-style:none;padding:0;margin:0}
.step{position:relative;padding-left:16px;margin-bottom:5px;list-style:none}
.step:last-child{margin-bottom:0}
.step__num{position:absolute;left:0;top:0;width:9px;height:9px;border-radius:2px;background:var(--orange);font-size:5.5px;font-weight:800;color:var(--white);display:flex;align-items:center;justify-content:center;z-index:1}
.steps::before{content:"";position:absolute;left:4px;top:9px;bottom:0;border-left:1px dashed rgba(255,255,255,.6)}
.step__title{font-size:7px;font-weight:800;margin-bottom:1px}
.other-services{left:0;top:300px;width:190px;text-align:center;color:var(--blue);font-weight:900;font-size:10px}
.service{position:absolute;width:74px;text-align:center}
.service .photo{position:relative;width:74px;height:34px;border:1.5px solid var(--blue)}
.service__label{font-size:5.4px;font-weight:600;margin-top:2px}

/* Back panel */
.value{position:absolute;left:16px;display:flex;align-items:center;gap:7px}
.value__icon{width:20px;height:20px;border-radius:50%;background:var(--blue);display:flex;align-items:center;justify-content:center}
.value__text{color:var(--orange);font-weight:900;font-size:8px;line-height:1.1}
.contact{left:0;top:290px;width:190px;text-align:center;color:var(--white)}
.contact__kicker{font-size:6.5px;letter-spacing:3px;font-weight:500}
.contact__call{font-size:9px;font-weight:800;line-height:1.2;margin-top:8px}
.phone-pill{display:inline-flex;align-items:center;gap:5px;background:var(--orange);border-radius:4px;padding:3px 8px;margin-top:6px;font-weight:800;font-size:10px}
.phone-pill__icon{width:11px;height:11px;background:var(--white);border-radius:2px;display:flex;align-items:center;justify-content:center}
.contact__web{font-size:6px;margin-top:6px;font-weight:500}

/* Brand name */
.brand{display:flex;align-items:center;justify-content:center;gap:5px;color:var(--blue);font-weight:800}
.brand__mark{width:10px;height:10px;background:var(--orange)}
.brand__sub{font-size:5.5px;letter-spacing:3.2px;text-align:center;font-weight:500;color:var(--ink)}
.brand--light{color:var(--white)}
.brand--light .brand__sub{color:var(--white)}

/* Cover */
.cover-brand{left:0;top:44px;width:190px}
.cover-brand .brand{font-size:17px}
.cover-head{left:14px;top:332px;width:166px;color:var(--white)}
.cover-head h1{font-weight:900;font-size:13px;line-height:1.1;letter-spacing:.2px}

/* About */
.panel--about{background:var(--orange-deep)}
.about{left:14px;top:26px;width:162px;color:var(--white)}
.about .rule{background:var(--white)}
.service-list{position:absolute;left:14px;top:256px;width:162px;list-style:none;color:var(--white)}
.service-list li{font-weight:800;font-size:6.8px;margin-bottom:7px;display:flex;align-items:center;gap:5px}
.service-list li::before{content:"";width:4px;height:4px;background:var(--white)}

/* Inside text panels */
.block{left:14px;width:162px}
.block .h-panel{color:var(--ink)}
</style>
</head>
<body>

<!-- OUTSIDE SPREAD -->
<section class="spread spread--outside">

  <!-- Inside flap: crime scene -->
  <article class="panel">
    <svg class="panel__shapes" viewBox="0 0 190 420" aria-hidden="true">
      <path d="M0 0H190V268Q95 272 0 292Z" fill="var(--blue)"/>
      <path d="M0 297Q95 277 190 273" stroke="var(--orange)" stroke-width="3" fill="none"/>
    </svg>
    <div class="abs crime">
      <h2 class="h-panel">Crime Scene &amp; Trauma Cleanup</h2>
      <span class="rule"></span>
      <p class="copy">At Brookvale Restoration we understand the impact of such a devastating incident. Our certified and experienced technicians possess compassion and respect for the situation and an unwavering attention to detail. Our trauma scene recovery team has the following four objectives in mind when responding to your call:</p>
    </div>
    <ol class="steps">
      <li class="step"><span class="step__num">1</span><div class="step__title">Safety and Well Being</div><div class="copy">The safety and well being of your family or the occupants of the building</div></li>
      <li class="step"><span class="step__num">2</span><div class="step__title">Disinfection</div><div class="copy">The disinfection of any pathogens at the site</div></li>
      <li class="step"><span class="step__num">3</span><div class="step__title">Removal</div><div class="copy">The disinfection/removal of the causes of the contaminates</div></li>
      <li class="step"><span class="step__num">4</span><div class="step__title">Customer Satisfaction</div><div class="copy">Customer satisfaction, easing our customer's burden and relieving any additional stress or concern regarding the cleaning of their property and areas where the incident occurred.</div></li>
    </ol>
    <h3 class="abs other-services">OTHER SERVICES</h3>
    <div class="service" style="left:14px;top:316px">
      <div class="photo" role="img" aria-label="Technician in protective suit disinfecting an office" style="background:linear-gradient(135deg,#e8b93a,#f3f0e2 55%,#6f8fb0)"></div>
      <div class="service__label">Covid-19 Cleaning</div>
    </div>
    <div class="service" style="left:102px;top:316px">
      <div class="photo" role="img" aria-label="Carpet being cleaned with a vacuum" style="background:linear-gradient(135deg,#3c68a8,#b9c3cf 60%,#8e98a4)"></div>
      <div class="service__label">Carpet &amp; Furniture Cleaning</div>
    </div>
    <div class="service" style="left:14px;top:368px">
      <div class="photo" role="img" aria-label="Pile of boxes and junk outside a house" style="background:linear-gradient(135deg,#9fb0bf,#c99a4e 60%,#6b7b4a)"></div>
      <div class="service__label">Junk Removal</div>
    </div>
    <div class="service" style="left:102px;top:368px">
      <div class="photo" role="img" aria-label="Asbestos danger tape across a doorway" style="background:linear-gradient(135deg,#3a3f46,#c8282a 55%,#1e2226)"></div>
      <div class="service__label">Asbestos Removal</div>
    </div>
  </article>

  <!-- Back panel -->
  <article class="panel">
    <div class="photo" role="img" aria-label="Empty room with white walls being restored" style="left:0;top:100px;width:190px;height:170px;background:linear-gradient(160deg,#cbc7bd,#efece6 45%,#b8b2a6)"></div>
    <svg class="panel__shapes" viewBox="0 0 190 420" aria-hidden="true">
      <path d="M0 100Q95 134 190 96V112Q95 150 0 116Z" fill="var(--blue)"/>
      <path d="M0 258Q95 290 190 250V420H0Z" fill="var(--orange)"/>
      <path d="M0 265Q95 298 190 258V420H0Z" fill="var(--blue)"/>
    </svg>
    <div class="value" style="top:34px">
      <span class="value__icon"><svg width="10" height="12" viewBox="0 0 10 12"><path d="M3 0H7L6 2L8 9L5 12L2 9L4 2Z" fill="#fff"/></svg></span>
      <span class="value__text">PROFESSIONALISM</span>
    </div>
    <div class="value" style="top:64px">
      <span class="value__icon"><svg width="12" height="12" viewBox="0 0 12 12"><circle cx="6" cy="4" r="2.6" fill="#fff"/><path d="M1 12Q6 5 11 12Z" fill="#fff"/></svg></span>
      <span class="value__text">WORLD CLASS<br>CUSTOMER SERVICE</span>
    </div>
    <div class="abs contact">
      <div class="contact__kicker">CONTACT US</div>
      <div class="brand brand--light" style="font-size:13px;margin-top:8px"><span class="brand__mark"></span>Brookvale</div>
      <div class="brand__sub" style="color:#fff">RESTORATION</div>
      <div class="contact__call">24/7 Emergency Service<br>Call Now!!!</div>
      <div class="phone-pill">
        <span class="phone-pill__icon"><svg width="7" height="7" viewBox="0 0 10 10"><path d="M2 0L4 2.5L3 4Q4 6 6 7L7.5 6L10 8L8.5 10Q3 9.5 0 2Z" fill="var(--orange)"/></svg></span>
        (555) 014-2290
      </div>
      <div class="contact__web">www.brookvalerestoration.com</div>
    </div>
  </article>

  <!-- Front cover -->
  <article class="panel">
    <div class="photo" role="img" aria-label="Restoration worker in orange coveralls and hard hat kneeling by a toolbox" style="left:0;top:130px;width:190px;height:190px;background:linear-gradient(150deg,#8fa79a,#d8dcd6 45%,#e0552a 70%,#c9c7c2)"></div>
    <svg class="panel__shapes" viewBox="0 0 190 420" aria-hidden="true">
      <path d="M0 128Q95 108 190 124V142Q95 126 0 150Z" fill="var(--blue)"/>
      <path d="M0 292Q95 286 190 318V420H0Z" fill="var(--orange)"/>
      <path d="M0 304Q95 298 190 332V420H0Z" fill="var(--blue)"/>
    </svg>
    <div class="abs cover-brand">
      <div class="brand"><span class="brand__mark"></span>Brookvale</div>
      <div class="brand__sub">RESTORATION</div>
    </div>
    <div class="abs cover-head">
      <h1>EXCEPTIONAL CUSTOMER SERVICE AND SATISFACTION</h1>
      <span class="rule"></span>
      <p class="copy" style="font-size:6px">We demonstrate honesty, integrity, and reliability in all phases of our work. We will strive to meet or exceed your expectations from start to finish</p>
    </div>
  </article>
</section>

<!-- INSIDE SPREAD -->
<section class="spread spread--inside">

  <!-- About -->
  <article class="panel panel--about">
    <div class="abs about">
      <h2 class="h-panel">About Us</h2>
      <span class="rule"></span>
      <div class="copy">
        <p>Our mission at Brookvale Restoration and Cleaning is to provide our customers with the highest level of services for all their emergency restoration and cleaning needs, with understanding, integrity, and professionalism.</p>
        <p>Because we are a local cleaning &amp; restoration company we like to keep our focus on giving back to our community and meeting our customers every day as we go about life. We seek to make our customers feel like more than just another job - we make it our goal to treat our customers like they are our neighbors, friends, and family, because that's what they are.</p>
        <p>You will get the highest quality service from our industry certified and trained staff, and the warmth and kindness you expect from your neighbors, family, and friends. Our vision is to become the number one choice and recommended local cleaning and restoration company on the North Shore, partnering with agents, realtors, homeowners and managers.</p>
      </div>
    </div>
    <ul class="service-list">
      <li>MOLD REMEDIATION</li>
      <li>SEWAGE CLEANUP</li>
      <li>FLOOD WATER CLEANUP</li>
      <li>ENCAPSULATION</li>
      <li>EXTRACTION AND DRYING</li>
      <li>FIRE RECOVERY</li>
      <li>BASEMENT RESTORATION</li>
    </ul>
  </article>

  <!-- Water & fire -->
  <article class="panel">
    <svg class="panel__shapes" viewBox="0 0 190 420" aria-hidden="true">
      <path d="M0 0H190V12Q95 14 0 26Z" fill="var(--blue)"/>
      <path d="M0 30Q95 18 190 16" stroke="var(--orange)" stroke-width="2.5" fill="none"/>
      <path d="M0 408Q95 398 190 396V420H0Z" fill="var(--blue)"/>
    </svg>
    <div class="abs block" style="top:40px">
      <h2 class="h-panel">Water Damage</h2>
      <span class="rule"></span>
      <p class="copy">Some people underestimate the damage that water can cause in parts of their property where water is not supposed to be. There is often a misconception that a few inches of water in your living room isn't much, but in reality, that "little" amount of water can create a devastating amount of damage. There have been cases where a little bit of water had caused damage that amount to upwards of a few thousand dollars, particularly because they didn't immediately call water damage restoration specialists for help. A couple of inches of water can damage expensive carpets, furniture, appliances, and other belongings. A little water can also affect floors, such as breaking down the glue that holds floor planks down, or causing wooden floors to swell. Walls become stained, and electrical outlets hit by flooding will also have to be replaced.</p>
    </div>
    <div class="photo photo--framed" role="img" aria-label="Couple catching leaking water in blue buckets at home" style="left:14px;top:222px;width:162px;height:74px;background:linear-gradient(135deg,#c7c0b5,#e9e4dc 45%,#2f63c4 75%,#5a6470)"></div>
    <div class="abs block" style="top:306px">
      <h2 class="h-panel">Fire &amp; Smoke Damage</h2>
      <span class="rule"></span>
      <p class="copy">Fire and smoke can leave behind soot, odors and hidden damage long after the flames are out. Our team acts fast to secure the property, remove residue, deodorize every room and restore surfaces, so your home is safe, clean and comfortable again.</p>
    </div>
  </article>

  <!-- Weather & mold -->
  <article class="panel">
    <svg class="panel__shapes" viewBox="0 0 190 420" aria-hidden="true">
      <path d="M0 0H190V12Q95 14 0 26Z" fill="var(--blue)"/>
      <path d="M0 30Q95 18 190 16" stroke="var(--orange)" stroke-width="2.5" fill="none"/>
      <path d="M0 408Q95 398 190 396V420H0Z" fill="var(--orange)"/>
      <path d="M0 412Q95 403 190 401V420H0Z" fill="var(--blue)"/>
    </svg>
    <div class="abs block" style="top:40px">
      <h2 class="h-panel">Weather Damage</h2>
      <span class="rule"></span>
      <div class="copy">
        <p>We are not sure of natural calamities that can happen anywhere, anytime. It can be anything like storm, lightning, earthquake that creates a huge loss and damage to properties. These are the situations that are very frustrating as we don't have the idea or experience to handle them. These needs to be handled by experts and professional teams so the things can be normal and back in shape as early as possible.</p>
        <p>We are professional and experts in handling these situations and help homeowners to get their property back in shape as efficiently as possible. Our professional teams treat all property damage with immense care.</p>
      </div>
    </div>
    <div class="photo photo--framed" role="img" aria-label="Storm cloud with lightning over open plains" style="left:14px;top:186px;width:162px;height:62px;background:linear-gradient(180deg,#3f5876,#c9d2da 40%,#6b7f93 70%,#3d4a3a)"></div>
    <div class="abs block" style="top:256px">
      <h2 class="h-panel">Mold</h2>
      <p class="copy" style="margin-top:4px">The development of Mold comes with moisture, excessive water, flooding, and many type of water leakages. This mold growth is huge threat to the belongings when it grows. It should be handled at first sight as it grows at fast rate and change the appearance of things. If left unchecked, it could result in reduced indoor air quality and an unsafe environment.</p>
    </div>
    <div class="photo photo--framed" role="img" aria-label="Black mold on a wall beside a window" style="left:14px;top:346px;width:162px;height:46px;background:linear-gradient(90deg,#e4e4e2,#d4d4d0 45%,#5a5a55 55%,#dcdcda 70%,#f4f5f6)"></div>
  </article>
</section>

</body>
</html>
```